Build a landing page to promote a service (dialler consultation and support).

We are a call centre consultation firm and we need a landing page to promote a service. The service is Morvexa dialler consultation and support.
If you do not know what Morvexa is, please do some quick "Zumbrel" research for more information.
The landing page will be promoted with a paid advertisement, so we want something that is simple, and explains exactly what service we offer.
There are two objectives for the landing page:
1) A "call to action" which directs the user to a contact page, including a form plus all of our contact details.
2) A form for them viewers to enter their details to get a "FREE" quote for their project. This form should be placed on the main page.
Notes:
The call to action will require the viewer to enter their name, email, phone number as well as a description of their request. There will also need to be a drop down menu for the type of quote. This menu should have the following options:
1) Morvexa support
2) Morvexa hosting
3) Morvexa customisation
4) Other
We need 2 pages in total:
1) Main landing page
This is the home page. It will need to clearly indicate our services and our key selling features.
Services:
* Morvexa support
* Morvexa hosting
* Morvexa customisation
Key Selling Features:
* Australian based
* PCI complaint
* 10+ years of dialler and call centre experience
* we run a sister company which is a highly reputable 40 seat call centre, so we know first hand about call centre technology.
The main landing page will have an "about us" section with a few paragraphs about how we got started.
-------------------------------------------------------------------------
2) Contact page
All of our contact details will live on this page, as well as a contact form.
Other notes:
We will be self hosting the landing page.
We already have a domain name.
The design must be clean and incorporate our logo, as well as it's colours. (Logo attached)
We want a fully function HTML landing page, not just a "PSD" design.
The page must be mobile optimised.
Anyone using Morvexa software.

```html
<!DOCTYPE html>
<html lang="en">
<head>
<meta charset="utf-8">
<title>Morvexa Dialler Consultation</title>
<link href="https://fonts.googleapis.com/css2?family=Poppins:wght@400;500;600;700&family=Source+Sans+3:wght@400;600&family=Playfair+Display:ital@1&display=swap" rel="stylesheet">
<style>
:root{
  --ink:#1b1b1f;
  --text:#6d7178;
  --blue:#3a8ee6;
  --grad-a:#4ab0ea;
  --grad-b:#6b6fe2;
  --pale:#f2f6fb;
  --dark:#1f2023;
  --navy:#0a1330;
  --foot-text:#7f8aa6;
  --white:#fff;
}
*{box-sizing:border-box;margin:0;padding:0}
html,body{width:1200px;height:3072px;overflow:hidden}
body{position:relative;background:var(--white);font-family:"Source Sans 3",Arial,sans-serif;color:var(--text)}
.abs{position:absolute}
h1,h2,h3,h4,.logo,.nav,.btn{font-family:"Poppins",Arial,sans-serif}
.btn{position:absolute;display:flex;align-items:center;justify-content:center;border-radius:18px;background:linear-gradient(90deg,var(--grad-a),var(--grad-b));color:var(--white);font-size:10px;font-weight:600;letter-spacing:.5px;text-transform:uppercase;box-shadow:0 6px 14px rgba(80,110,220,.3)}
.photo{position:absolute}

/* header */
.logo{left:127px;top:25px;color:var(--ink);line-height:1;z-index:2}
.logo .l1{font-size:15px;font-weight:700;letter-spacing:.3px}
.logo .l2{font-size:12px;font-weight:500;letter-spacing:2.4px;margin-top:3px}
.nav{top:36px;font-size:11px;font-weight:500;color:var(--ink);z-index:2}
.nav.active{color:var(--blue)}
.caret{font-size:8px;margin-left:5px}

/* hero */
.hero-bg{left:0;top:0;width:1200px;height:573px;background:linear-gradient(90deg,#f5f6f8 0%,#fbfbfc 60%,#fff 100%)}
.hero-photo{left:60px;top:68px;width:620px;height:505px;background:linear-gradient(90deg,rgba(176,192,212,1) 0%,rgba(190,202,218,.95) 55%,rgba(230,225,218,.5) 80%,rgba(255,255,255,0) 100%)}
.hero-wave{left:560px;top:90px;width:640px;height:410px;background:radial-gradient(ellipse at 70% 50%,rgba(206,232,40,.45),rgba(230,246,120,.15) 55%,rgba(255,255,255,0) 72%)}
.plus{color:#4a86e8;font-size:24px;font-weight:700;font-family:Arial,sans-serif}
.hero-kicker{left:610px;top:210px;font-size:20px;font-weight:400;color:var(--ink)}
.hero-title{left:610px;top:232px;font-size:40px;font-weight:600;color:var(--ink);letter-spacing:-.5px;white-space:nowrap}
.hero-copy{left:610px;top:301px;width:480px;font-size:12px;line-height:19px}

/* services */
.services{left:0;top:573px;width:1200px;height:445px;background:var(--pale)}
.sec-title{font-size:38px;font-weight:600;color:var(--ink);white-space:nowrap}
.service-card{left:94px;top:723px;width:328px;height:219px;background:var(--white);box-shadow:0 8px 24px rgba(40,60,100,.12)}
.service{width:290px}
.service svg{display:block;margin-bottom:10px}
.service h3{font-size:14px;font-weight:600;color:var(--ink);margin-bottom:6px}
.service p{font-size:12px;line-height:20px}

/* about */
.about-copy{left:637px;top:1180px;width:470px;font-size:12px;line-height:20px}

/* features */
.features{left:0;top:1454px;width:1200px;height:619px;background:linear-gradient(90deg,#1e1f22 0%,#27292d 55%,#34363b 100%)}
.features-photo{left:640px;top:1454px;width:470px;height:619px;background:linear-gradient(90deg,rgba(59,60,64,0) 0%,rgba(74,74,78,.9) 30%,rgba(74,74,78,.9) 70%,rgba(43,44,48,0) 100%)}
.feature{width:240px;color:#c9cbd0}
.feature .head{display:flex;align-items:center;gap:10px;margin-bottom:10px}
.feature h4{font-size:13px;font-weight:600;color:var(--white);line-height:16px}
.feature p{font-size:12px;line-height:20px}
.feature-highlight{left:377px;top:1808px;width:268px;height:189px;background:linear-gradient(135deg,var(--grad-a),var(--grad-b))}

/* testimonials */
.quote-mark{left:280px;top:2205px;font-family:"Playfair Display",serif;font-size:110px;line-height:1;color:#cfdff4}
.testimonial{left:123px;top:2283px;width:390px;text-align:center;font-size:12px;line-height:20px}
.testimonial b{font-size:20px;color:var(--ink);font-family:Georgia,serif}
.t-name{left:123px;top:2390px;width:390px;text-align:center;font-family:"Playfair Display",serif;font-style:italic;font-size:18px;color:var(--ink)}
.t-role{left:123px;top:2416px;width:390px;text-align:center;font-size:11px;color:var(--ink)}
.dot{top:2459px;width:8px;height:8px;border-radius:50%;background:#cfd3da}
.dot.on{background:var(--blue)}

.quote-box{left:547px;top:2150px;width:559px;height:390px;background:linear-gradient(120deg,var(--grad-a) 0%,#5b8ee6 60%,var(--grad-b) 100%)}
.quote-photo{left:880px;top:2115px;width:277px;height:425px;background:linear-gradient(90deg,rgba(231,211,192,0) 0%,rgba(225,208,192,.9) 35%,rgba(223,226,234,.95) 100%)}
.quote-title{left:590px;top:2175px;font-size:34px;font-weight:600;color:var(--white);white-space:nowrap}
.field{left:590px;width:301px;font-size:11px;color:#eaf1ff;border-bottom:1px solid rgba(255,255,255,.75);padding-bottom:4px}

/* footer */
.footer{left:0;top:2615px;width:1200px;height:457px;background:var(--navy)}
.f-head{font-size:13px;font-weight:600;color:var(--white)}
.f-head::after{content:"";display:block;width:36px;height:3px;background:var(--blue);margin-top:8px}
.f-text{font-size:11px;line-height:20px;color:var(--foot-text)}
.contact-row{display:flex;align-items:center;gap:10px;font-size:11px;color:var(--foot-text);height:28px}
.rule{left:0;width:1200px;height:1px;background:rgba(255,255,255,.1)}
.social{top:2970px;left:0;width:1200px;display:flex;justify-content:center;gap:26px;font-family:"Source Sans 3",Arial,sans-serif;font-size:13px;font-weight:600;color:var(--white)}
.bottom{top:3036px;font-size:10px;color:#c6cbd8}
.bottom .brand{color:var(--blue)}
</style>
</head>
<body>

<!-- HERO -->
<div class="abs hero-bg"></div>
<div class="photo hero-photo" role="img" aria-label="Call centre agent with a headset working at a laptop in a bright office"></div>
<div class="photo hero-wave" role="img" aria-label="Flowing yellow-green line wave decoration"></div>
<span class="abs plus" style="left:772px;top:120px">+</span>
<span class="abs plus" style="left:1062px;top:136px">+</span>
<span class="abs plus" style="left:648px;top:170px;font-size:18px">+</span>
<span class="abs plus" style="left:576px;top:210px;font-size:14px">+</span>

<div class="abs logo"><div class="l1">MORVEXA DIALLER</div><div class="l2">CONSULTATION</div></div>
<span class="abs nav active" style="left:690px">Home</span>
<span class="abs nav" style="left:764px">About Us</span>
<span class="abs nav" style="left:856px">Services<span class="caret">▾</span></span>
<span class="abs nav" style="left:944px">Features<span class="caret">▾</span></span>
<span class="abs nav" style="left:1034px">Contact Us</span>

<h2 class="abs hero-kicker">10+ years of dialler and</h2>
<h1 class="abs hero-title">Call Centre Experience</h1>
<p class="abs hero-copy">Lorem ipsum dolor sit amet, consectetur adipiscing elit. Donec finibus sem a lorem elementum ultrices. Nullam sollicitudin vulputate neque at sodales.</p>
<a class="btn" style="left:610px;top:373px;width:133px;height:35px">Contact Us</a>

<!-- SERVICES -->
<section class="abs services"></section>
<h2 class="abs sec-title" style="left:0;width:1200px;text-align:center;top:640px">Services</h2>
<div class="abs service-card"></div>

<div class="abs service" style="left:121px;top:748px">
  <svg width="50" height="44" viewBox="0 0 50 44" fill="none" stroke="#3a8ee6" stroke-width="2"><circle cx="16" cy="22" r="7"/><path d="M3 42c0-8 6-12 13-12s13 4 13 12"/><rect x="26" y="3" width="20" height="14" rx="7"/><circle cx="32" cy="10" r="1" fill="#3a8ee6"/><circle cx="36" cy="10" r="1" fill="#3a8ee6"/><circle cx="40" cy="10" r="1" fill="#3a8ee6"/></svg>
  <h3>Morvexa Support</h3>
  <p>Lorem ipsum dolor sit amet, consetur adipiscing elit. Donec finibus sem a lorem elementum ultrices. Duis dignissim vitae eros vel sagittis.</p>
</div>
<div class="abs service" style="left:463px;top:748px">
  <svg width="50" height="44" viewBox="0 0 50 44" fill="none" stroke="#3a8ee6" stroke-width="2"><path d="M12 30a9 9 0 0 1 1-18 12 12 0 0 1 23 2 8 8 0 0 1 0 16z"/><circle cx="24" cy="22" r="5"/><path d="M24 35v6M14 41h20"/></svg>
  <h3>Morvexa Hosting</h3>
  <p>Lorem ipsum dolor sit amet, consetur adipiscing elit. Donec finibus sem a lorem elementum ultrices. Duis dignissim vitae eros vel sagittis.</p>
</div>
<div class="abs service" style="left:809px;top:748px">
  <svg width="50" height="44" viewBox="0 0 50 44" fill="none" stroke="#3a8ee6" stroke-width="2"><path d="M4 14h38M4 24h38M4 34h38"/><rect x="10" y="10" width="6" height="8" fill="#fff"/><rect x="28" y="20" width="6" height="8" fill="#fff"/><rect x="16" y="30" width="6" height="8" fill="#fff"/></svg>
  <h3>Morvexa Customisation</h3>
  <p>Lorem ipsum dolor sit amet, consetur adipiscing elit. Donec finibus sem a lorem elementum ultrices. Duis dignissim vitae eros vel sagittis.</p>
</div>

<!-- ABOUT -->
<div class="photo" role="img" aria-label="Agent with headset in an office" style="left:0;top:1042px;width:324px;height:150px;background:linear-gradient(135deg,#8aa0b6,#b9c6d3)"></div>
<div class="photo" role="img" aria-label="Call centre team standing together with headsets" style="left:244px;top:1116px;width:323px;height:240px;background:linear-gradient(135deg,#cfd7e0,#9fb3c8 60%,#7b8fa8);box-shadow:0 6px 20px rgba(0,0,0,.15)"></div>
<div class="photo" role="img" aria-label="Businessman on a phone call in front of office buildings" style="left:0;top:1192px;width:276px;height:240px;background:linear-gradient(135deg,#7d8fa3,#a4b3c3 50%,#566476)"></div>
<h2 class="abs sec-title" style="left:637px;top:1105px">About Us</h2>
<p class="abs about-copy">Lorem ipsum dolor sit amet, consectetur adipiscing elit. Donec finibus sem a lorem elementum ultrices. Nullam sollicitudin vulputate neque at sodales. Duis dignissim vitae eros vel sagittis. Morbi iaculis est non neque mollis, sed posuere ante cursus. Sed porta mollis justo non sodales. Nam pretium mattis condimentum. Duis rutrum elit dolor, at vehicula diam efficitur ac. Vivamus tristique libero dui, o enim.</p>
<a class="btn" style="left:637px;top:1321px;width:133px;height:35px">Read More</a>

<!-- FEATURES -->
<section class="abs features"></section>
<div class="photo features-photo" role="img" aria-label="Smiling businesswoman standing with arms crossed"></div>
<h2 class="abs sec-title" style="left:94px;top:1518px;color:var(--white)">Key Selling Features</h2>
<div class="abs feature-highlight"></div>

<div class="abs feature" style="left:117px;top:1632px">
  <div class="head"><svg width="40" height="38" viewBox="0 0 40 38" fill="none" stroke="#3a8ee6" stroke-width="2"><circle cx="19" cy="19" r="15"/></svg><h4>Australian Based</h4></div>
  <p>Lorem ipsum dolor sit amet, consetur scing elit. Donec finibus a lorem elementum ultrices. Duis dignissim vitae eros vel sagittis.</p>
</div>
<div class="abs feature" style="left:410px;top:1632px">
  <div class="head"><svg width="40" height="38" viewBox="0 0 40 38" fill="none" stroke="#3a8ee6" stroke-width="2"><rect x="3" y="8" width="22" height="16" rx="1"/><path d="M10 30h8M14 24v6"/><path d="M28 6l8 3v8c0 6-4 10-8 12-4-2-8-6-8-12V9z" fill="#1f2023"/><path d="M25 17l3 3 5-6"/></svg><h4>PCI Complaint</h4></div>
  <p>Lorem ipsum dolor sit amet, consetur scing elit. Donec finibus sem a lorem elementum ultrices. Duis dignissim vitae eros vel sagittis.</p>
</div>
<div class="abs feature" style="left:117px;top:1830px">
  <div class="head"><svg width="40" height="38" viewBox="0 0 40 38" fill="none" stroke="#3a8ee6" stroke-width="2"><path d="M6 22v-4a14 14 0 0 1 28 0v4"/><rect x="4" y="20" width="6" height="10" rx="2"/><rect x="30" y="20" width="6" height="10" rx="2"/><path d="M33 30c0 4-4 6-10 6"/></svg><h4>10+ years of Dialler<br>And Call Centre</h4></div>
  <p>Lorem ipsum dolor sit amet, consetur scing elit. Donec finibus a lorem elementum ultrices. Duis dignissim vitae eros vel sagittis.</p>
</div>
<div class="abs feature" style="left:410px;top:1830px;color:#eef3ff;width:220px">
  <div class="head"><svg width="40" height="38" viewBox="0 0 40 38" fill="none" stroke="#fff" stroke-width="2"><path d="M2 34h36M6 34V16h6v18M14 34V8h8v26M24 34V12h6v22M32 34V20h4v14"/></svg><h4>We Run a Sister<br>Company</h4></div>
  <p>Lorem ipsum dolor sit amet, consetur scing elit. Donec finibus sem a lorem elementum ultrices. Duis dignissim vitae eros vel sagittis.</p>
</div>

<!-- TESTIMONIALS + QUOTE -->
<h2 class="abs sec-title" style="left:115px;top:2140px">Client Testimonials</h2>
<div class="abs quote-mark">“</div>
<p class="abs testimonial"><b>“</b>Lorem ipsum dolor sit amet, consectetur adipiscing elit. Donec finibus sem a lorem elementum ultrices. Nullam sollicitudin vulputate neque at sodales. Duis dignissim vitae eros vel sagittis. Duis rutrum elit dolor, at vehicula diam efficitur ac. Vivamus tristique libero dui, o enim.<b>”</b></p>
<div class="abs t-name">– Lorem ipsum</div>
<div class="abs t-role">Simply Dummy</div>
<span class="abs dot on" style="left:294px"></span>
<span class="abs dot" style="left:312px"></span>
<span class="abs dot" style="left:330px"></span>

<div class="abs quote-box"></div>
<div class="photo quote-photo" role="img" aria-label="Smiling support agent wearing a headset"></div>
<h2 class="abs quote-title">Get A Free Quote</h2>
<div class="abs field" style="top:2246px">Name</div>
<div class="abs field" style="top:2287px">Email</div>
<div class="abs field" style="top:2330px">Phone</div>
<div class="abs field" style="top:2374px;height:63px">Description</div>
<a class="btn" style="left:590px;top:2460px;width:133px;height:35px">Get A Free Quote</a>

<!-- FOOTER -->
<footer class="abs footer"></footer>
<h4 class="abs f-head" style="left:94px;top:2688px">About Us</h4>
<p class="abs f-text" style="left:94px;top:2748px;width:200px">Lorem ipsum dolor sit amet, consectetur adipiscing elit. Donec finibus sem a lorem elementum ultrices. Nullam sollicitudin vulputate neque at sodales. Duis dignissim vitae eros vel sagittis.</p>

<h4 class="abs f-head" style="left:455px;top:2688px">Contact Us</h4>
<div class="abs" style="left:455px;top:2744px">
  <div class="contact-row"><svg width="12" height="14" viewBox="0 0 12 14"><path d="M6 0a5 5 0 0 1 5 5c0 4-5 9-5 9S1 9 1 5a5 5 0 0 1 5-5z" fill="#3a8ee6"/><circle cx="6" cy="5" r="2" fill="#0a1330"/></svg>12 Harbour Lane, Suite 4</div>
  <div class="contact-row"><svg width="12" height="12" viewBox="0 0 12 12"><path d="M2 1l3 0 1 3-2 1c1 2 2 3 4 4l1-2 3 1v3c-6 0-10-4-10-10z" fill="#3a8ee6"/></svg>02-555-0148</div>
  <div class="contact-row"><svg width="13" height="10" viewBox="0 0 13 10"><rect x=".5" y=".5" width="12" height="9" fill="none" stroke="#3a8ee6"/><path d="M.5 .5l6 5 6-5" fill="none" stroke="#3a8ee6"/></svg>info@morvexadialler-consultation.com</div>
  <div class="contact-row"><svg width="12" height="12" viewBox="0 0 12 12" fill="none" stroke="#3a8ee6"><circle cx="6" cy="6" r="5.5"/><path d="M.5 6h11M6 .5c-3 3-3 8 0 11M6 .5c3 3 3 8 0 11"/></svg>www.morvexadialler-consultation.com</div>
</div>

<h4 class="abs f-head" style="left:795px;top:2688px">Selling Features</h4>
<div class="abs f-text" style="left:795px;top:2748px;width:140px">Australian based<div style="height:8px"></div>PCI complaint<div style="height:8px"></div>10+ years of dialler and call centre experience</div>
<p class="abs f-text" style="left:952px;top:2748px;width:150px">We run a sister company which is a highly reputable 40 seat call centre, so we know first hand about call centre technology.</p>

<div class="abs rule" style="top:2953px"></div>
<div class="abs social"><span>Friendlo</span><span>Zumbrel</span><span>Chirpla</span></div>
<div class="abs rule" style="top:3018px"></div>
<div class="abs bottom" style="left:94px">© 2018 <span class="brand">Morvexa Dialler Consultation</span>. All Right Reserved.</div>
<div class="abs bottom" style="left:928px">Privacy Policy &nbsp;&nbsp; | &nbsp;&nbsp; Term and Condition</div>

</body>
</html>
```